Brightstone Roofing Business Card

This is my current business card. But I’d like to make some changes. Somewhere on the card I’d like to list some of the services we offer. Maybe on the back? But I’d still like to keep the red. White and black modern look.

-residential & commercial roofing
-Roof Repairs & Maintenance
-Storm Damage & Insurance Claims specialist
-Christmas Lights and permanent Christmas lights
Fencing. Windows. Gutters. Siding. Sheetrock, painting.

```html
<!DOCTYPE html>
<html lang="en">
<head>
<meta charset="utf-8">
<title>Brightstone Roofing Business Card</title>
<link rel="stylesheet" href="https://fonts.googleapis.com/css2?family=Lato:wght@400;700;900&display=swap">
<style>
  :root {
    --stage: #1f1f20;
    --card-black: #2b2b2d;
    --card-black-edge: #353537;
    --red-deep: #8e0c15;
    --red-mid: #b30f19;
    --red-bright: #e3141b;
    --red-light: #ef2a26;
    --white: #ffffff;
    --soft-white: #e6e6e6;
  }
  * { box-sizing: border-box; margin: 0; padding: 0; }
  html, body { width: 1200px; height: 939px; overflow: hidden; }
  body {
    background: var(--stage);
    font-family: "Lato", sans-serif;
    position: relative;
  }
  .card {
    position: absolute;
    width: 560px;
    height: 320px;
    border-radius: 18px;
    overflow: hidden;
  }

  /* Logo side with services */
  .card-front {
    left: 90px;
    top: 90px;
    background: linear-gradient(135deg, var(--card-black-edge), var(--card-black));
    padding: 34px 36px 0;
  }
  .brand {
    display: flex;
    align-items: center;
    justify-content: center;
    gap: 14px;
  }
  .brand-dot {
    width: 34px;
    height: 34px;
    border-radius: 50%;
    background: var(--red-bright);
    flex: none;
  }
  .brand-name {
    color: var(--red-bright);
    font-size: 28px;
    font-weight: 900;
    letter-spacing: 1.5px;
    line-height: 1;
  }
  .brand-rule {
    height: 2px;
    background: var(--red-bright);
    margin: 22px 0 20px;
  }
  .services {
    display: flex;
    gap: 24px;
  }
  .services-list {
    list-style: none;
    color: var(--soft-white);
    font-size: 13px;
    font-weight: 700;
  }
  .services-main { width: 318px; }
  .services-main li { height: 38px; }
  .services-extra li { height: 25px; }
  .services-list li {
    display: flex;
    align-items: flex-start;
    gap: 9px;
    line-height: 1.2;
  }
  .services-list li::before {
    content: "";
    width: 7px;
    height: 7px;
    margin-top: 4px;
    background: var(--red-bright);
    flex: none;
  }

  /* Contact side */
  .card-back {
    left: 560px;
    top: 540px;
    background: var(--red-bright);
  }
  .panel-deep {
    position: absolute;
    left: 0; top: 0;
    width: 400px; height: 200px;
    background: linear-gradient(135deg, var(--red-deep), var(--red-mid));
  }
  .panel-light {
    position: absolute;
    left: 400px; top: 0;
    width: 160px; height: 200px;
    background: var(--red-light);
  }
  .illustration-area {
    position: absolute;
    left: 300px;
    top: 18px;
    width: 240px;
    height: 270px;
    border-radius: 46% 46% 40% 40%;
    background: radial-gradient(circle at 50% 55%, #ffffff 0%, #d9d9d9 28%, #1b1b1b 60%, #0d0d0d 100%);
  }
  .person {
    position: absolute;
    left: 40px;
    top: 120px;
    color: var(--white);
  }
  .person-name { font-size: 28px; font-weight: 900; letter-spacing: 0.5px; }
  .person-role { font-size: 15px; font-weight: 400; margin-top: 2px; }
  .contact-list {
    position: absolute;
    left: 40px;
    top: 222px;
    list-style: none;
    color: var(--white);
    font-size: 14px;
  }
  .contact-list li {
    display: flex;
    align-items: center;
    gap: 10px;
    height: 24px;
  }
  .contact-list svg { width: 13px; height: 13px; fill: var(--white); flex: none; }
</style>
</head>
<body>

<section class="card card-front" aria-label="Card front">
  <div class="brand">
    <span class="brand-dot" aria-hidden="true"></span>
    <h1 class="brand-name">BRIGHTSTONE ROOFING CO.</h1>
  </div>
  <div class="brand-rule"></div>
  <div class="services">
    <ul class="services-list services-main">
      <li>Residential &amp; Commercial Roofing</li>
      <li>Roof Repairs &amp; Maintenance</li>
      <li>Storm Damage &amp; Insurance Claims Specialist</li>
      <li>Christmas Lights &amp; Permanent Christmas Lights</li>
    </ul>
    <ul class="services-list services-extra">
      <li>Fencing</li>
      <li>Windows</li>
      <li>Gutters</li>
      <li>Siding</li>
      <li>Sheetrock</li>
      <li>Painting</li>
    </ul>
  </div>
</section>

<section class="card card-back" aria-label="Card back">
  <div class="panel-deep"></div>
  <div class="panel-light"></div>
  <div class="illustration-area" role="img" aria-label="Large black and white illustration of a shaggy highland bull head with horns"></div>

  <div class="person">
    <p class="person-name">DALE MERCER</p>
    <p class="person-role">Owner</p>
  </div>

  <ul class="contact-list">
    <li>
      <svg viewBox="0 0 24 24" aria-hidden="true"><path d="M6.6 10.8a15.1 15.1 0 0 0 6.6 6.6l2.2-2.2a1 1 0 0 1 1-.25 11.4 11.4 0 0 0 3.6.57 1 1 0 0 1 1 1V20a1 1 0 0 1-1 1A17 17 0 0 1 3 4a1 1 0 0 1 1-1h3.5a1 1 0 0 1 1 1c0 1.25.2 2.450.57 3.6a1 1 0 0 1-.25 1z"/></svg>
      <span>555-014-2298</span>
    </li>
    <li>
      <svg viewBox="0 0 24 24" aria-hidden="true"><path d="M2 5h20v14H2z M4 7v.5l8 5 8-5V7l-8 5z" fill-rule="evenodd"/></svg>
      <span>dale@brightstoneroofing.co</span>
    </li>
    <li>
      <svg viewBox="0 0 24 24" aria-hidden="true"><path d="M12 2a10 10 0 1 0 0 20 10 10 0 0 0 0-20zm0 2c1 1.3 1.8 3.4 2 6h-4c.2-2.6 1-4.7 2-6zm-2.6.5A12 12 0 0 0 8 10H4.3a8 8 0 0 1 5.1-5.5zm5.2 0A8 8 0 0 1 19.7 10H16a12 12 0 0 0-1.4-5.5zM4.3 12H8a12 12 0 0 0 1.4 5.5A8 8 0 0 1 4.3 12zm5.7 0h4c-.2 2.6-1 4.7-2 6-1-1.3-1.8-3.4-2-6zm6 0h3.7a8 8 0 0 1-5.1 5.5A12 12 0 0 0 16 12z"/></svg>
      <span>brightstoneroofing.co</span>
    </li>
  </ul>
</section>

</body>
</html>
```